meditation/yoga retreat eco village ashram commune website

There is a group of 20-30 people living in the jungle of mexico. We all came together from all walks of life to help built a paradise on earth. This is a meditation ashram resort that is built by a living enlightenment master, a modern day buddha master Swami Veleth Tarunai. It's his vision and his love that he wants to share to the world.

The eco village project is on a 19 hectares forest land with a cenote (natural pond) as the heart centre surrounded by beautiful tropical gardens. This unique village is conceived in a mystical mayan circle as an oasis for creative arts crafts music and dance, mayan wisdom, eastern ayurveda, yoga, vipassana, meditation and silent retreat for the science of inner transformation this eco development will offer residents and visitors the experience of nature, silence, tranquility, meditativeness and a compassionate space for growth and flowering of human consciousness.

we are creating an inner science mystery school where we will offer ancient mayan traditions, buddhist vipassana, tibetan teachings, yoga, patanjali yoga, pranayama, we will also offer meditations and therapies like mystic rose, born again, no mind, painting group, breath, prana healing, primal, work as meditation all therapies and meditations will be offered for free we accept donations out of gratitude

The NEW DOMAIN for this website will be - www.VELMIRAKA.example

This is our old website - http://tarunaiveleth.example/o/miraka/
it is outdated and we haven't done anything to it in the past 5 years. Now that we are about to open to the world, we want a fresh new look that will captivate our audience. Please take a moment to browse our website to get an idea of who we are.

Also please check out our facebook page, you will see all our past events, upcoming events with pics and videos.
www.facebook.com/velmiraka
www.instagram.com/velmiraka

We have 3 festivals coming up, they are as follows.
Yoga festival - https://www.facebook.com/events/5203917264803159/
Art festival - https://www.facebook.com/events/5209384617250436/
Thai massage - https://www.facebook.com/events/6480215937402951/

Do not use any of the pictures from the old website, it is outdated, most are just drawings and sketches. I have zipped up some great pictures for you to use, ...also feel free to use anything from facebook/instagram as well.

For menu, also we will have sub-categories menu for each as well.

HOME
NEWS
THE PROJECT
EVENTS
VIDEOS
PHOTOS
TICKETS
RESIDENTIAL
DONATE
CONTACT

Things to include for main page.
*Upcoming Events
*Previous Pics/Videos of Past Events (grab them from our facebook page)
*Show some great construction building, moon palapa, star palapa, welcome center, etc..
*Maybe a section where the master can say a message.
*Mediation/Yoga section
*Residential Booking
*Facebook page, *twitter feed, instagram, youtube channel
Updates

Target Market(s)

meditation, yoga, art, dance festivals

Industry/Entity Type

Group

Number of Pages Required

1 page

Requirements
Must have
• we are looking for something classy, elegant, yet simple...stay away from traditional, give it a really cool modern touch.

```html
<!DOCTYPE html>
<html lang="en">
<head>
<meta charset="utf-8">
<title>Velmira — Eco Village Retreat</title>
<link rel="stylesheet" href="https://fonts.googleapis.com/css2?family=Roboto:wght@300;400;500&family=Montserrat:wght@400;500;600&family=Oswald:wght@400&display=swap">
<style>
  :root {
    --sidebar: #2a2f33;
    --accent: #e0262b;
    --white: #ffffff;
    --menu-text: #b9bcbf;
    --section-bg: #f3f3f3;
    --ink: #1e1e1e;
    --muted: #7d7d7d;
    --hero-shade: rgba(0, 0, 0, 0.18);
  }
  * { margin: 0; padding: 0; box-sizing: border-box; }
  html, body { width: 1200px; height: 1058px; overflow: hidden; }
  body { font-family: "Roboto", sans-serif; background: var(--white); position: relative; }

  .hero { position: absolute; left: 0; top: 0; width: 1200px; height: 617px; }
  .hero-photo {
    position: absolute; left: 0; top: 0; width: 1006px; height: 617px;
    background:
      radial-gradient(ellipse 60% 45% at 50% 62%, #6f7f52 0%, rgba(95,110,70,0) 70%),
      linear-gradient(180deg, #5e4a33 0%, #6b5a3e 28%, #56663f 52%, #4e5b38 72%, #7a6d58 88%, #6a5f4e 100%);
  }
  .hero-photo::after {
    content: ""; position: absolute; inset: 0; background: rgba(20, 18, 14, 0.25);
  }
  .hero-edge { position: absolute; top: 0; height: 617px; width: 58px; background: var(--hero-shade); }
  .hero-edge.left { left: 0; }
  .hero-edge.right { left: 948px; }

  .brand-name {
    position: absolute; left: 0; width: 1200px; top: 168px;
    text-align: center; color: var(--white); font-weight: 500; font-size: 60px;
    letter-spacing: 6px; line-height: 60px;
  }

  .hero-tagline {
    position: absolute; left: 0; width: 1200px; top: 302px;
    text-align: center; color: var(--white); font-weight: 300; font-size: 26px; line-height: 32px;
  }
  .hero-prev { position: absolute; left: 108px; top: 298px; }
  .hero-close { position: absolute; left: 969px; top: 301px; }
  .find-more {
    position: absolute; left: 0; width: 1200px; top: 526px; text-align: center;
    font-family: "Montserrat", sans-serif; font-size: 13px; letter-spacing: 2.6px;
    color: #ddd; font-weight: 500;
  }
  .find-more-arrow { position: absolute; left: 594px; top: 569px; }

  .social { position: absolute; left: 22px; top: 234px; list-style: none; display: flex; flex-direction: column; gap: 30px; }
  .social li { width: 15px; height: 15px; border-radius: 50%; background: #e8e8e8; }

  .sidebar { position: absolute; left: 1006px; top: 0; width: 194px; height: 617px; background: var(--sidebar); }
  .main-nav { position: absolute; left: 26px; top: 120px; list-style: none; }
  .main-nav li {
    font-family: "Montserrat", sans-serif; font-size: 12.5px; letter-spacing: 1.6px;
    color: var(--menu-text); height: 31.8px; line-height: 18px; position: relative;
  }
  .main-nav li.active { color: var(--accent); }
  .main-nav li.active::before {
    content: ""; position: absolute; left: -25px; top: 9px; width: 20px; height: 1px; background: #8a8d90;
  }
  .contact-btn {
    position: absolute; left: 0; top: 470px; width: 122px; height: 38px;
    border: 1.5px solid var(--accent); color: var(--accent);
    font-family: "Montserrat", sans-serif; font-size: 12.5px; letter-spacing: 1.6px;
    display: flex; align-items: center; justify-content: center;
  }

  .events-head { position: absolute; left: 0; top: 617px; width: 1200px; height: 159px; background: var(--section-bg); }
  .events-title {
    position: absolute; left: 0; width: 1200px; top: 687px; text-align: center;
    font-family: "Montserrat", sans-serif; font-weight: 600; font-size: 16px; letter-spacing: 3.4px; color: var(--ink);
  }
  .events-title span { color: var(--accent); }

  .event-card { position: absolute; top: 776px; width: 400px; height: 282px; overflow: hidden; }
  .event-card .photo { position: absolute; inset: 0; }
  .event-card .name {
    position: absolute; left: 0; width: 100%; text-align: center;
    color: var(--white); font-weight: 300; font-size: 22px; line-height: 24px;
  }
  .event-yoga { left: 0; }
  .event-yoga .photo { background: linear-gradient(160deg, #3d4232 0%, #2c3326 45%, #5a3a3e 80%, #3b2d2c 100%); }
  .event-yoga .photo::after { content: ""; position: absolute; inset: 0; background: rgba(0,0,0,0.2); }
  .event-yoga .name { top: 172px; }

  .event-art { left: 400px; }
  .event-art .date-box { position: absolute; left: 0; top: 0; width: 400px; height: 159px; background: var(--white); text-align: center; }
  .event-art .date { font-family: "Oswald", sans-serif; font-size: 36px; color: var(--ink); margin-top: 34px; line-height: 40px; }
  .event-art .place { font-size: 13.5px; color: var(--muted); margin-top: 10px; }
  .event-art .time { font-size: 13.5px; color: var(--muted); margin-top: 4px; display: flex; align-items: center; justify-content: center; gap: 5px; }
  .event-art .photo { top: 159px; background: linear-gradient(120deg, #3a3430 0%, #4c4a48 40%, #3c4e5e 70%, #2a2a2c 100%); }
  .event-art .photo::after { content: ""; position: absolute; inset: 0; background: rgba(0,0,0,0.15); }
  .event-art .notch {
    position: absolute; left: 191px; top: 159px; width: 0; height: 0;
    border-left: 9px solid transparent; border-right: 9px solid transparent; border-top: 9px solid var(--white);
  }
  .event-art .name { top: 198px; }

  .event-massage { left: 800px; }
  .event-massage .photo { background: radial-gradient(ellipse 45% 40% at 55% 70%, #b55a78 0%, rgba(180,90,120,0) 70%), linear-gradient(170deg, #4a4a44 0%, #3a3c36 50%, #5e5550 100%); }
</style>
</head>
<body>
  <header class="hero">
    <div class="hero-photo" role="img" aria-label="Open palapa with thatched roof and central timber column, jungle beyond"></div>
    <div class="hero-edge left"></div>
    <div class="hero-edge right"></div>

    <ul class="social" aria-label="Social channels">
      <li aria-label="Social page"></li>
      <li aria-label="Photo feed"></li>
      <li aria-label="Video channel"></li>
      <li aria-label="News feed"></li>
    </ul>

    <h1 class="brand-name">VELMIRA</h1>

    <svg class="hero-prev" width="14" height="20" viewBox="0 0 14 20" aria-label="Previous slide"><polyline points="11,2 3,10 11,18" fill="none" stroke="#e0262b" stroke-width="2.2"/></svg>
    <p class="hero-tagline">An Eco Village! -&nbsp; Conceived in mystical<br>mayan circle to retreat silent for the science<br>of inner transformation.</p>
    <svg class="hero-close" width="14" height="14" viewBox="0 0 14 14" aria-label="Close"><path d="M2 2L12 12M12 2L2 12" stroke="#fff" stroke-width="2.4"/></svg>

    <div class="find-more">FIND OUT MORE</div>
    <svg class="find-more-arrow" width="12" height="14" viewBox="0 0 12 14" aria-hidden="true"><path d="M6 1V11" stroke="#fff" stroke-width="2.2"/><polyline points="1.5,7 6,11.5 10.5,7" fill="none" stroke="#fff" stroke-width="2.2"/></svg>

    <nav class="sidebar">
      <ul class="main-nav">
        <li class="active">HOME</li>
        <li>NEWS</li>
        <li>THE PROJECT</li>
        <li>EVENTS</li>
        <li>VIDEOS</li>
        <li>PHOTOS</li>
        <li>TICKETS</li>
        <li>RESIDENTIAL</li>
        <li>DONATE</li>
      </ul>
      <div class="contact-btn">CONTACT</div>
    </nav>
  </header>

  <section class="events-head"></section>
  <h2 class="events-title"><span>UPCOMING</span> EVENTS</h2>

  <article class="event-card event-yoga">
    <div class="photo" role="img" aria-label="Yoga practitioner stretching among flowering garden"></div>
    <h3 class="name">Shiva Moon Yoga<br>Festival</h3>
  </article>

  <article class="event-card event-art">
    <div class="date-box">
      <div class="date">18/20</div>
      <div class="place">Nov, 77520 Costa Serena, Mexico</div>
      <div class="time">
        <svg width="11" height="11" viewBox="0 0 12 12" aria-hidden="true"><circle cx="6" cy="6" r="4.8" fill="none" stroke="#555" stroke-width="1.5"/><path d="M6 3.3V6H8" fill="none" stroke="#555" stroke-width="1.3"/></svg>
        10 pm
      </div>
    </div>
    <div class="photo" role="img" aria-label="Artist painting a colourful mural canvas"></div>
    <div class="notch"></div>
    <h3 class="name">Heart Festival</h3>
  </article>

  <article class="event-card event-massage">
    <div class="photo" role="img" aria-label="Open hand holding a pink lotus flower"></div>
  </article>
</body>
</html>
```